New business card for civil engineering company - "Keystone Audit"

We need a business card designed for our new structural engineering company.

The company name is "Keystone Audit" logo files attached.

We would like the following:
* Two-sided card
* Simple design

Information to be placed on the card:
Name - Marcus Dellow
Job Title - Director / Structural Engineer
Credentials - BEng(Hons), CPEng, CMengNZ, IntPE(NZ)
Email - marcus.dellow@keystoneaudit.co.nz
mobile - 0219364058
website - www.keystoneaudit.co.nz

```html
<!DOCTYPE html>
<html lang="en">
<head>
<meta charset="utf-8">
<title>Keystone Audit – Business Card</title>
<link rel="stylesheet" href="https://fonts.googleapis.com/css2?family=Titillium+Web:ital,wght@0,400;0,700;1,400&display=swap">
<style>
  :root {
    --page: #e6e6e6;
    --charcoal: #3d3d3d;
    --yellow: #ffe93f;
    --white: #ffffff;
    --faint: rgba(255, 255, 255, 0.12);
    --ink: #3d3d3d;
  }
  html, body {
    margin: 0;
    padding: 0;
    width: 1004px;
    height: 1200px;
    overflow: hidden;
    background: var(--page);
    font-family: "Titillium Web", "Helvetica Neue", Arial, sans-serif;
  }
  .canvas {
    position: relative;
    width: 1004px;
    height: 1200px;
  }
  .card {
    position: absolute;
    left: 26px;
    width: 946px;
    height: 558px;
    background: var(--charcoal);
    overflow: hidden;
  }
  .card--front { top: 30px; }
  .card--back { top: 614px; }
  .card__band {
    position: absolute;
    inset: 0;
    width: 100%;
    height: 100%;
  }
  .brand {
    position: absolute;
    margin: 0;
    font-weight: 700;
    text-transform: uppercase;
    white-space: nowrap;
    letter-spacing: 0.03em;
    line-height: 1;
  }
  .brand--faint {
    left: 150px;
    top: 440px;
    font-size: 50px;
    color: var(--faint);
  }
  .brand--front {
    right: 26px;
    top: 232px;
    font-size: 30px;
    color: var(--ink);
  }
  .brand--back {
    left: 60px;
    top: 430px;
    font-size: 34px;
    color: var(--ink);
  }
  .contact {
    position: absolute;
    right: 54px;
    top: 56px;
    text-align: right;
    color: var(--white);
  }
  .contact__name {
    margin: 0;
    font-size: 38px;
    font-weight: 700;
    letter-spacing: 0.05em;
    line-height: 1.1;
    text-transform: uppercase;
  }
  .contact__role {
    margin: 4px 0 0;
    font-size: 20px;
    font-weight: 700;
    letter-spacing: 0.08em;
    text-transform: uppercase;
  }
  .contact__credentials {
    margin: 20px 0 0;
    font-size: 22px;
    font-style: italic;
    color: var(--yellow);
    letter-spacing: 0.03em;
  }
  .contact__details {
    list-style: none;
    margin: 68px 0 0;
    padding: 0;
    font-size: 18px;
    line-height: 28px;
    letter-spacing: 0.03em;
  }
</style>
</head>
<body>
<main class="canvas">

  <section class="card card--front" aria-label="Card front">
    <svg class="card__band" viewBox="0 0 946 558" preserveAspectRatio="none" aria-hidden="true">
      <polygon points="383,0 946,0 946,558" fill="var(--yellow)"/>
    </svg>
    <p class="brand brand--faint" aria-hidden="true">Keystone Audit</p>
    <p class="brand brand--front">Keystone Audit</p>
  </section>

  <section class="card card--back" aria-label="Card back">
    <svg class="card__band" viewBox="0 0 946 558" preserveAspectRatio="none" aria-hidden="true">
      <polygon points="0,0 565,558 0,558" fill="var(--yellow)"/>
    </svg>
    <p class="brand brand--back">Keystone Audit</p>
    <div class="contact">
      <h1 class="contact__name">Marcus Dellow</h1>
      <p class="contact__role">Director / Structural Engineer</p>
      <p class="contact__credentials">BEng(Hons), CPEng, CMengNZ, IntPE(NZ)</p>
      <ul class="contact__details">
        <li>marcus.dellow@keystoneaudit.co.nz</li>
        <li>0219364058</li>
        <li>www.keystoneaudit.co.nz</li>
      </ul>
    </div>
  </section>

</main>
</body>
</html>
```